Startup Consultancy - Brochure Design

This needs to be a digital and potential hardcopy of a glossy brochure, designed to really catch the eye of prospective clients and draw them in. I am looking for something alternative from the "usual", but equally in keeping with the IT industry that the business operate in. The business specifically focuses on Print & Document Software and Technology solutions, and this should be considered in the design.

Target Market(s)

SMB and Corporate End Users, + Technology Resellers

Industry/Entity Type

Information Technology

Other font styles liked:
• Avenir

Colors
9d9d9d
848484
c3c3c3
e8e8e8
ffffff
eaeaea
0255a3
3176b5
85acd3

Requirements
Must have
• Company logo displayed on the front, plus any other relevant placements in pages
• Must follow the colour/style in some way of the website (www.brantwellconsultancy.co.uk)
Nice to have
• Some kind of infographical style in the brochure would be good, perhaps around the service listings

```html
<!DOCTYPE html>
<html lang="en">
<head>
<meta charset="utf-8">
<title>Brantwell Strategic Consultancy – Brochure</title>
<link href="https://fonts.googleapis.com/css2?family=Mulish:wght@400;600;700;800&display=swap" rel="stylesheet">
<style>
:root{
  --blue:#0255a3;
  --blue-mid:#3176b5;
  --blue-light:#85acd3;
  --grey-dark:#484848;
  --grey:#848484;
  --grey-mid:#9d9d9d;
  --grey-light:#c3c3c3;
  --paper:#e8e8e8;
  --white:#ffffff;
  --navy:#0b1b33;
  --ink:#222;
  --stage:#2b2b2b;
}
*{margin:0;padding:0;box-sizing:border-box}
html,body{width:842px;height:1200px;overflow:hidden;background:var(--stage)}
body{position:relative;font-family:"Mulish",sans-serif;color:var(--ink)}
.spread{position:absolute;left:0;width:842px;height:590px;overflow:hidden}
.spread--outer{top:0}
.spread--inner{top:610px}
.page{position:absolute;top:0;width:421px;height:590px;overflow:hidden}
.page--left{left:0}.page--right{left:421px}
.abs{position:absolute}
.photo{position:absolute;inset:0}
.title{position:absolute;font-weight:600;font-size:15px;letter-spacing:.2px;text-transform:uppercase;color:var(--ink)}
.title .accent{color:var(--blue)}
.title-rule{position:absolute;width:34px;height:3px;background:var(--blue)}
.subhead{position:absolute;font-weight:700;font-size:10px}
.body-copy{position:absolute;font-size:6.6px;line-height:8.6px;text-align:justify;color:#333}
.body-copy p{margin-bottom:7px}
.contact-list{position:absolute;list-style:none;font-size:8.4px;color:#333}
.contact-list li{display:flex;gap:7px;align-items:flex-start;margin-bottom:8px}
.contact-list svg{flex:none;margin-top:1px}
.wordmark{position:absolute;font-weight:700;color:#4a4a4a;letter-spacing:.3px}
.mark-square{position:absolute;background:#4a4a4a}
.social{position:absolute;width:22px;height:22px;border-radius:50%;background:var(--blue-mid)}
.foot-band{position:absolute;left:0;right:0;bottom:0;height:14px;background:#3a3a3a}
/* cover */
.welcome{position:absolute;right:36px;text-align:right;color:var(--white)}
.welcome h1{font-weight:700;font-size:22px;line-height:27px;letter-spacing:.3px}
.welcome .rule{width:58px;height:3px;background:var(--white);margin:7px 0 10px auto}
.welcome p{font-size:12px;line-height:15px;font-weight:400}
.url-bar{position:absolute;left:0;right:0;bottom:0;height:32px}
.url-bar span{position:absolute;right:36px;top:9px;font-size:11.5px;color:var(--white);display:flex;gap:6px;align-items:center}
/* inner */
.section-head{position:absolute;display:flex;align-items:center;gap:10px}
.section-head .icon{width:16px;height:12px;background:var(--grey-mid)}
.section-head .title{position:static}
.dark .title,.dark .subhead{color:var(--white)}
.dark .body-copy{color:#c9d3e0;font-size:5.6px;line-height:7.4px}
.dark .section-head .icon{background:var(--grey-light)}
.band{position:absolute;left:0;right:0}
.band--blue{background:var(--blue)}
.band--light{background:linear-gradient(160deg,#f2f2f2,#d6d6d6)}
.services-for{position:absolute;color:var(--white)}
.services-for small{display:block;font-size:10.5px;font-weight:400}
.services-for strong{display:block;font-size:12px;font-weight:700;letter-spacing:.2px}
.engage{position:absolute;color:var(--white);font-size:12px;font-weight:600}
.ticks{position:absolute;list-style:none}
.ticks li{display:flex;gap:8px;align-items:flex-start}
.ticks--training li{font-size:8.4px;font-weight:700;color:#222;margin-bottom:7px}
.ticks--tender li{font-size:5.6px;line-height:7.2px;color:#dbe6f2;margin-bottom:7px}
.steps{position:absolute;list-style:none;width:345px}
.steps li{font-size:5.6px;line-height:7.2px;color:#555;text-align:justify}
.steps b{color:var(--blue);font-size:6.6px;font-weight:700}
.tender-title{position:absolute;color:var(--white);font-size:12.5px;font-weight:600;display:flex;gap:10px;align-items:center}
.tender-title .icon{width:16px;height:12px;background:var(--grey-light)}
</style>
</head>
<body>

<!-- OUTER SPREAD -->
<section class="spread spread--outer">
  <div class="page page--left">
    <div class="photo" role="img" aria-label="Hazy city skyline photograph in pale blue and grey tones with soft rounded tile shapes" style="background:linear-gradient(180deg,#c9d6e4 0%,#d9dee3 45%,#c6c9cc 75%,#b9bcbf 100%)"></div>

    <h2 class="title" style="left:45px;top:42px">About <span class="accent">Us</span></h2>
    <div class="title-rule" style="left:45px;top:63px"></div>
    <div class="subhead" style="left:45px;top:79px">Taking a different path</div>
    <div class="body-copy" style="left:45px;top:96px;width:312px">
      <p>We provide services to End User organisations of various sizes, shapes and styles, ranging from SMB through to Enterprise business and even Government, across a range of vertical markets, helping to create forward thinking, future proofed strategic design for Print &amp; Document Workflow solutions – critically however as an entirely independent approach, without any affiliations to manufacturers, software houses or resellers.</p>
      <p>Our expertise, experience and services also support Channel Partners, OEM's and Distributors, providing guidance and design services for Print &amp; Document Workflow strategies, promoting a customer led focus, efficiency and our own core values of honesty and reliability.</p>
      <p>As a group of very experienced, highly skilled and senior members of the IT/Print/Document Solutions industry, we grew tired of the lack of true, un-biased and trusted advice and support within the industry that both Channel Partners and End Users alike would often receive.</p>
      <p>We don't sell hardware. We don't even sell software.</p>
      <p>We remain independent of any manufacturers and are not affiliated to any partner or dealer. What we do provide however is trusted, valuable consultancy, design and advice.</p>
    </div>

    <h2 class="title" style="left:45px;top:440px">Contact <span class="accent">Us</span></h2>
    <div class="title-rule" style="left:45px;top:461px"></div>
    <ul class="contact-list" style="left:45px;top:477px">
      <li><svg width="8" height="10" viewBox="0 0 8 10"><path d="M4 0a3.5 3.5 0 0 0-3.5 3.5C.5 6 4 10 4 10s3.5-4 3.5-6.5A3.5 3.5 0 0 0 4 0z" fill="#3176b5"/><circle cx="4" cy="3.5" r="1.2" fill="#fff"/></svg><span>18 Harlow Lane, London,<br>EC1V 4PT</span></li>
      <li><svg width="8" height="9" viewBox="0 0 8 9"><circle cx="4" cy="4.5" r="3.6" fill="none" stroke="#3176b5" stroke-width="1"/><path d="M2.6 2.6l1 1-.5.7 1.1 1.1.7-.5 1 1-.8.8c-1.2 0-3.3-2.1-3.3-3.3z" fill="#3176b5"/></svg><span>0203 555 0142</span></li>
      <li><svg width="8" height="9" viewBox="0 0 8 9"><rect x=".5" y="2" width="7" height="5" fill="none" stroke="#3176b5"/><path d="M.5 2l3.5 3 3.5-3" fill="none" stroke="#3176b5"/></svg><span>enquiries@brantwellconsultancy.co.uk</span></li>
      <li><svg width="8" height="9" viewBox="0 0 8 9"><circle cx="4" cy="4.5" r="3.5" fill="#3176b5"/><path d="M.5 4.5h7M4 1v7" stroke="#fff" stroke-width=".6"/></svg><span>www.brantwellconsultancy.co.uk</span></li>
    </ul>

    <div class="mark-square" style="left:322px;top:492px;width:10px;height:10px"></div>
    <div class="wordmark" style="left:290px;top:505px;font-size:17px">Brantwell</div>
    <div class="social" style="left:307px;top:532px"></div>
    <div class="social" style="left:337px;top:532px"></div>
    <div class="foot-band"></div>
  </div>

  <div class="page page--right">
    <div class="photo" role="img" aria-label="Photograph of a businessman's hand drawing a glowing network diagram with circular technology icons over a city backdrop" style="background:linear-gradient(135deg,#cfd4da 0%,#8d97a4 30%,#2f3e55 55%,#1c2a40 75%,#5d6878 100%)"></div>
    <svg class="abs" style="left:0;top:0" width="421" height="590" viewBox="0 0 421 590">
      <polygon points="0,482 421,362 421,590 0,590" fill="#0255a3"/>
      <polygon points="0,482 421,362 421,392 0,520" fill="#3176b5" opacity=".35"/>
    </svg>
    <div class="mark-square" style="left:360px;top:86px;width:14px;height:14px"></div>
    <div class="wordmark" style="right:36px;top:108px;font-size:29px">Brantwell</div>

    <div class="welcome" style="top:430px">
      <h1>WELCOME TO<br>A NEW APPROACH</h1>
      <div class="rule"></div>
      <p>We have a range of services<br>suitable for a range of clients including End Users,<br>Channel Partners, OEM's and Distributors.</p>
    </div>

    <div class="url-bar">
      <svg class="abs" style="left:0;top:0" width="421" height="32" viewBox="0 0 421 32"><polygon points="190,0 421,0 421,32 170,32" fill="#3a3a3a"/></svg>
      <span><svg width="11" height="11" viewBox="0 0 11 11"><circle cx="5.5" cy="5.5" r="4.8" fill="none" stroke="#fff"/><ellipse cx="5.5" cy="5.5" rx="2" ry="4.8" fill="none" stroke="#fff" stroke-width=".8"/><path d="M.7 5.5h9.6" stroke="#fff" stroke-width=".8"/></svg>www.brantwellconsultancy.co.uk</span>
    </div>
  </div>
</section>

<!-- INNER SPREAD -->
<section class="spread spread--inner">
  <div class="page page--left">
    <div class="dark">
      <div class="photo" role="img" aria-label="Dark blue night-time city photograph with light trails" style="height:321px;background:linear-gradient(180deg,#081528 0%,#0f2340 55%,#1a3a63 80%,#0c1c33 100%)"></div>

      <div class="section-head" style="left:45px;top:36px"><div class="icon"></div><h2 class="title">Why <span class="accent">choose us?</span></h2></div>
      <div class="subhead" style="left:45px;top:74px">An alternative and innovative approach</div>
      <div class="body-copy" style="left:45px;top:92px;width:345px">
        <p>We take pride, satisfaction and enjoyment from providing clients with clear, non-bias advice. Our determination to stand alone in the industry without commercial affiliations or ties to any particular manufacturer, channel partner or software developer sets us apart from the rest.</p>
        <p>We consistently monitor the marketplace and industry, ensuring we are up to speed on trends and technology as well as research and understanding, to deliver professional, experienced and justifiable advice and planning.</p>
        <p>We also maintain memberships with leading analyst groups and more, along with having representation on European advisory boards with a view to positively contributing to the imaging and printing industry standards.</p>
        <p>It is our aim to be the most trusted consultancy in our industry, but to do this we have to earn it.</p>
      </div>

      <div class="section-head" style="left:45px;top:211px"><div class="icon"></div><h2 class="title">How do we <span class="accent">do that?</span></h2></div>
      <div class="body-copy" style="left:45px;top:248px;width:345px">
        <p>Honest and open advice, transparency in our approach and the integrity to ensure we inform our clients if we cannot provide services that are suitable or to the high standards expected by you or us – if we can't help we will tell you so openly, no fuss, no over promising.</p>
        <p>Our consultancy services also ensure you are aware and prepared for potential pitfalls, complexities and challenges associated with the world of Print &amp; Document solutions.</p>
      </div>
    </div>

    <div class="band band--blue" style="top:321px;height:128px"></div>
    <div class="services-for" style="left:45px;top:340px"><small>Services for</small><strong>CHANNEL PARTNERS, OEM'S OR DISTRIBUTORS</strong></div>
    <div class="services-for" style="left:45px;top:379px"><small>Services for</small><strong>END USER ORGANISATIONS</strong></div>
    <div class="engage" style="left:45px;top:418px">How do Brantwell engage on a project, large or small?</div>

    <div class="band band--light" style="top:449px;height:141px"></div>
    <div class="section-head" style="left:45px;top:473px"><div class="icon"></div><h2 class="title">Training <span class="accent">services</span></h2></div>
    <ul class="ticks ticks--training" style="left:45px;top:513px">
      <li><svg width="9" height="9" viewBox="0 0 9 9"><path d="M1 5l2.2 2.2L8 1.5" fill="none" stroke="#0255a3" stroke-width="1.6"/></svg>Creation and agreement of training objectives including content specifics</li>
      <li><svg width="9" height="9" viewBox="0 0 9 9"><path d="M1 5l2.2 2.2L8 1.5" fill="none" stroke="#0255a3" stroke-width="1.6"/></svg>Skills summary of staff, including (if applicable) separation of training groups</li>
      <li><svg width="9" height="9" viewBox="0 0 9 9"><path d="M1 5l2.2 2.2L8 1.5" fill="none" stroke="#0255a3" stroke-width="1.6"/></svg>Training template and plan provided</li>
    </ul>
  </div>

  <div class="page page--right">
    <div class="band band--light" style="top:0;height:449px"></div>

    <div class="section-head" style="left:45px;top:36px"><div class="icon"></div><h2 class="title">Strategy <span class="accent">design services</span></h2></div>
    <div class="subhead" style="left:45px;top:74px">A roadmap for your future</div>
    <ul class="steps" style="left:45px;top:92px">
      <li style="margin-bottom:6px"><b>Stakeholder Interviews &amp; Feedback</b> – a key element right at the beginning of the process. It is important for us to understand your organisation in detail, its specific areas of business, target markets, competitors and much more.</li>
      <li style="margin-bottom:6px"><b>Objective &amp; Goal Mapping</b> – where does your organisation need to get to with any new strategic design, what are the risk factors, and what are the key priorities.</li>
      <li style="margin-bottom:6px"><b>Departmental/Process Review</b> – what is done where in the current organisation structure, why and how.</li>
      <li style="margin-bottom:6px"><b>Gap Analysis</b> – understanding the gaps and areas to address between the current state and the short/mid-term and long term objectives and goals.</li>
      <li style="margin-bottom:6px"><b>Strategic Design Proposal</b> – based on all findings the new strategic design proposal can be created. This must then be agreed and signed off by all relevant stakeholders.</li>
      <li><b>Final Design &amp; Project Plan</b> – the final critical element is understanding how and more importantly when all elements of the new strategy can be implemented.</li>
    </ul>

    <div class="section-head" style="left:45px;top:238px"><div class="icon"></div><h2 class="title">Operational <span class="accent">design services</span></h2></div>
    <div class="subhead" style="left:45px;top:275px">A crucial success factor</div>
    <ul class="steps" style="left:45px;top:293px">
      <li style="margin-bottom:6px"><b>Stakeholder Interviews &amp; Feedback</b> – a key element right at the beginning of the process. It is important for us to understand your organisation in detail, its specific areas of business, operational dependencies, operational systems and much more.</li>
      <li style="margin-bottom:6px"><b>Objective &amp; Goal Mapping</b> – where does your organisation need to get to with any new operational design, what are the risk factors, and what are the key priorities.</li>
      <li style="margin-bottom:6px"><b>Departmental/Process Review</b> – what is done where in the current organisation structure, why and how.</li>
      <li style="margin-bottom:6px"><b>Gap Analysis</b> – understanding the gaps and areas to address between the current state and the short/mid-term and long term objectives and goals.</li>
      <li style="margin-bottom:6px"><b>Operational Design Proposal</b> – based on all findings the new operational design proposal can be created. This must then be agreed and signed off by all relevant stakeholders.</li>
      <li><b>Final Design &amp; Project Plan</b> – the final critical element is understanding how and more importantly when all elements of the new strategy can be implemented.</li>
    </ul>

    <div class="band band--blue" style="top:449px;height:141px"></div>
    <div class="tender-title" style="left:45px;top:463px"><div class="icon"></div>TENDER CONSULTANCY &amp; WRITING SERVICES</div>
    <ul class="ticks ticks--tender" style="left:45px;top:498px;width:345px">
      <li><svg width="9" height="9" viewBox="0 0 9 9" style="flex:none"><path d="M1 5l2.2 2.2L8 1.5" fill="none" stroke="#fff" stroke-width="1.6"/></svg>End User tenders and tender service requirements vary dramatically depending on elements such as organisation size, type and much more.</li>
      <li><svg width="9" height="9" viewBox="0 0 9 9" style="flex:none"><path d="M1 5l2.2 2.2L8 1.5" fill="none" stroke="#fff" stroke-width="1.6"/></svg>We assist End Users in everything from tender creation, support services in conjunction with existing teams and even tender review services, covering short to long term requirements.</li>
      <li><svg width="9" height="9" viewBox="0 0 9 9" style="flex:none"><path d="M1 5l2.2 2.2L8 1.5" fill="none" stroke="#fff" stroke-width="1.6"/></svg>We can also provide services supporting procurement or tender response analysis for End User organisations of all sizes.</li>
      <li><svg width="9" height="9" viewBox="0 0 9 9" style="flex:none"><path d="M1 5l2.2 2.2L8 1.5" fill="none" stroke="#fff" stroke-width="1.6"/></svg>If you would like to discuss how we may be able to help with any tender requirements, please feel free to get in touch.</li>
    </ul>
  </div>
</section>

</body>
</html>
```